Covid 19 Advertising Banner

1 - I want a banner ad for my website size - 940 x 297,
2 - Also i would like just a standard size ad that is the same but just a square size for facebook advertising.
I have attached a photo that we can use of one of my workers with a Dellavan electrical jumper on - maybe have this in the background blurred or something?
I have also attached an example of a different business "Harbour Volt" to show sorta what i'm trying to achieve.
The idea of this ad is to let people know that Dellavan Electrical is still open during Stage 4 restrictions.
Must have the type of work we are open for - Critical repairs to any premises where required for emergency or safety.
my website for reference - dellavanelectrical.com.au
i have attached the Dellavan Electrical Logo that this ad must have.
Please make sure my phone number is on the ad 0438157296 and my website as above.

```html
<!DOCTYPE html>
<html lang="en">
<head>
<meta charset="utf-8">
<title>Dellavan Electrical – Open During Stage 4</title>
<link href="https://fonts.googleapis.com/css2?family=Montserrat:wght@500;600;700;800&display=swap" rel="stylesheet">
<style>
  :root {
    --brand-blue: #1d6fbd;
    --navy: #1f4f8f;
    --body-grey: #5a5a5a;
    --bg-light: #f4f4f4;
    --bg-mid: #e4e4e4;
    --photo-tone: #4f86c4;
  }
  * { margin: 0; padding: 0; box-sizing: border-box; }
  html, body { width: 1200px; height: 380px; overflow: hidden; background: #ffffff; }
  .banner {
    position: relative;
    width: 1200px;
    height: 380px;
    overflow: hidden;
    font-family: 'Montserrat', Arial, sans-serif;
    background: linear-gradient(100deg, var(--bg-mid) 0%, var(--bg-light) 45%, #fafafa 100%);
  }
  .worker-photo {
    position: absolute;
    left: 0; top: 0;
    width: 345px; height: 380px;
    background: linear-gradient(90deg, var(--photo-tone) 0%, #8fb0d6 55%, rgba(228,228,228,0) 100%);
  }
  .headline {
    position: absolute;
    left: 357px; top: 18px;
    color: var(--brand-blue);
    font-weight: 800;
    font-size: 56px;
    line-height: 60px;
    white-space: nowrap;
  }
  .service-note {
    position: absolute;
    left: 358px; top: 156px;
    color: var(--body-grey);
    font-weight: 600;
    font-size: 25px;
    line-height: 32px;
    white-space: nowrap;
  }
  .call-line {
    position: absolute;
    left: 357px; top: 294px;
    color: var(--brand-blue);
    font-weight: 800;
    font-size: 36px;
    line-height: 44px;
    white-space: nowrap;
  }
  .brand {
    position: absolute;
    left: 802px; top: 272px;
    display: flex;
    align-items: center;
    gap: 12px;
  }
  .brand-square {
    width: 78px; height: 78px;
    background: var(--navy);
  }
  .brand-divider {
    width: 2px; height: 80px;
    background: var(--navy);
    opacity: 0.5;
  }
  .brand-text { display: flex; flex-direction: column; gap: 4px; }
  .brand-name {
    color: var(--navy);
    font-weight: 700;
    font-size: 24px;
    line-height: 26px;
    letter-spacing: 2px;
    text-transform: uppercase;
  }
  .brand-web {
    color: var(--navy);
    font-weight: 500;
    font-size: 13px;
    letter-spacing: 0.4px;
    white-space: nowrap;
  }
</style>
</head>
<body>
  <div class="banner">
    <div class="worker-photo" role="img" aria-label="Photo of an electrician in work gear stripping wires at a wall"></div>

    <h1 class="headline">We are still open for you<br>during Stage 4 restrictions</h1>

    <p class="service-note">Critical repairs to any premises where required for<br>emergency or safety</p>

    <p class="call-line">Call now 0438 157 296</p>

    <div class="brand">
      <div class="brand-square"></div>
      <div class="brand-divider"></div>
      <div class="brand-text">
        <span class="brand-name">Dellavan<br>Electrical</span>
        <span class="brand-web">www.dellavanelectrical.com.au</span>
      </div>
    </div>
  </div>
</body>
</html>
```